We are looking for a new website design for our SEO WEB Development Company. The URL is www.brellowcreativeworks.com

We want it to be a more powerful representation of what we do. We are also looking for a number of designers that we will give continuous business to every month. The persons design we choose will also get a proposal to complete 4 - 6 new designs for us every month for our clients.

Be creative as you can in your design submissions. We really want to stand out!

Just to give you an idea of what we like look at this site: http://www.tovandigitalstudio.com/

```html
<!DOCTYPE html>
<html lang="en">
<head>
<meta charset="utf-8">
<title>Brellow Interactive Group – Dallas Web Design &amp; Internet Marketing</title>
<link rel="stylesheet" href="https://fonts.googleapis.com/css2?family=Arimo:wght@400;700&family=Tinos:ital@1&display=swap">
<style>
  :root {
    --brand-orange: #f6b21c;
    --ink: #1a1a1a;
    --tab-dark: #141414;
    --tab-pink: #d45c9c;
    --chevron: #e0168c;
    --hero-light: #f4f4f4;
    --hero-mid: #c9c9c9;
    --hero-dark: #9c9c9c;
    --magenta: #b3117f;
    --green: #2f8a12;
    --blue: #0b63b3;
    --black: #101010;
    --orange: #f39616;
    --panel-top: #ffffff;
    --panel-bottom: #8a82c4;
    --frame: #3a3a3a;
    --follow-blue: #1f6fd1;
  }
  * { box-sizing: border-box; margin: 0; padding: 0; }
  html, body { width: 1200px; height: 898px; overflow: hidden; background: #fff; }
  .page { position: relative; width: 1200px; height: 898px; font-family: "Arimo", Arial, sans-serif; background: #fff; }

  /* navigation */
  .main-nav { position: absolute; top: 0; left: 0; width: 1200px; height: 106px;
    background: linear-gradient(#ffffff, #f1f1f1 70%, #d8d8d8); }
  .nav-tab { position: absolute; top: 61px; height: 42px; border-radius: 4px;
    background: linear-gradient(100deg, var(--tab-dark) 45%, #5a2a44 75%, var(--tab-pink));
    box-shadow: 0 2px 3px rgba(0,0,0,.35);
    color: #fff; font-weight: 700; font-size: 16px; display: flex; align-items: center; padding-left: 30px; }
  .nav-tab::before { content: ""; position: absolute; left: 10px; top: 12px; width: 9px; height: 18px;
    background: var(--chevron); clip-path: polygon(0 0, 45% 0, 100% 50%, 45% 100%, 0 100%, 55% 50%); }
  .nav-tab--home { font-size: 26px; }
  .nav-tab--home::before { background: #3fbf2a; }

  /* hero */
  .hero { position: absolute; top: 106px; left: 0; width: 1200px; height: 406px;
    background: linear-gradient(#e9e9e9, var(--hero-mid) 55%, var(--hero-dark));
    border-top: 3px solid #8a8a8a; }
  .brand-name { position: absolute; left: 38px; color: var(--brand-orange); font-weight: 700; font-size: 31px; }
  .banner-rail { position: absolute; left: 342px; top: 21px; width: 856px; height: 12px; background: #bdbdbd; }
  .banner { position: absolute; left: 342px; top: 38px; width: 856px; height: 175px;
    background: linear-gradient(100deg, #ffffff 0%, #dfe6ee 30%, #2c7fc2 55%, #0d3f86 80%, #0a2f6a 100%);
    border: 1px solid #999; }
  .banner-tagline { position: absolute; right: 8px; top: 60px; color: #fff; text-align: left; }
  .banner-tagline strong { display: block; font-size: 19px; letter-spacing: 2px; font-weight: 700; }
  .banner-tagline span { display: block; font-size: 13px; letter-spacing: 1px; margin-top: 2px; }

  .service { position: absolute; width: 192px; height: 84px; border-radius: 50%;
    background: radial-gradient(ellipse at 50% 30%, #ffffff, #e4e4e4 60%, #9a9a9a);
    box-shadow: 0 3px 5px rgba(0,0,0,.35); }
  .service-label { position: absolute; left: 12px; top: 10px; width: 168px; height: 64px; border-radius: 50%;
    display: flex; align-items: center; justify-content: center; text-align: center;
    color: #fff; font-weight: 700; font-size: 18px; line-height: 1.2;
    box-shadow: inset 0 -6px 10px rgba(0,0,0,.35), inset 0 6px 8px rgba(255,255,255,.35); }
  .service-label--small { font-size: 14px; }
  .service-label--tiny { font-size: 12px; }
  .is-magenta { background: var(--magenta); }
  .is-green { background: var(--green); }
  .is-blue { background: var(--blue); }
  .is-black { background: var(--black); }
  .is-orange { background: var(--orange); }

  /* content */
  .content { position: absolute; top: 512px; left: 0; width: 1200px; height: 386px; background: #e2e2e2;
    border-top: 3px solid var(--frame); }
  .panel { position: absolute; top: 8px; height: 370px;
    background: linear-gradient(var(--panel-top), #d9d6ee 45%, var(--panel-bottom));
    border: 2px solid var(--frame); font-family: "Tinos", "Times New Roman", serif; font-style: italic; color: var(--ink); }
  .panel--about { left: 8px; width: 878px; padding: 14px 26px; }
  .panel--quote { left: 894px; width: 302px; padding: 18px 0 0 28px; }
  .about-lead { font-size: 23.5px; line-height: 34px; }
  .about-body { font-size: 18.5px; line-height: 28px; margin-top: 20px; }
  .accent { color: var(--brand-orange); }

  .quote-intro { font-size: 22px; line-height: 34px; }
  .quote-button { position: absolute; left: 48px; top: 152px; width: 176px; height: 86px; border-radius: 50%;
    background: radial-gradient(ellipse at 50% 30%, #fff, #ddd 60%, #999); box-shadow: 0 3px 5px rgba(0,0,0,.3); }
  .quote-button span { position: absolute; left: 14px; top: 12px; width: 148px; height: 62px; border-radius: 50%;
    background: var(--blue); box-shadow: inset 0 -6px 10px rgba(0,0,0,.4);
    display: flex; align-items: center; justify-content: center; text-align: center;
    font-family: "Arimo", Arial, sans-serif; font-style: normal; color: #111; font-size: 14px; line-height: 28px; }
  .follow-title { position: absolute; right: 12px; top: 268px; font-family: "Arimo", Arial, sans-serif; font-style: normal;
    color: var(--follow-blue); font-size: 20px; }
  .social-list { position: absolute; left: 160px; top: 308px; width: 140px; display: grid;
    grid-template-columns: repeat(3, 28px); gap: 12px 20px; list-style: none; }
  .social-item { width: 28px; height: 28px; background: #2a3f6a; border-radius: 3px; }
</style>
</head>
<body>
<div class="page">
  <nav class="main-nav">
    <a class="nav-tab nav-tab--home" style="left:9px;width:171px">Home</a>
    <a class="nav-tab" style="left:205px;width:168px">Creative Design</a>
    <a class="nav-tab" style="left:401px;width:168px">Website Design</a>
    <a class="nav-tab" style="left:599px;width:168px">Internet Marketing</a>
    <a class="nav-tab" style="left:795px;width:168px">IT Consulting</a>
    <a class="nav-tab" style="left:994px;width:167px">Contact Us</a>
  </nav>

  <header class="hero">
    <div class="brand-name" style="top:50px">Brellow</div>
    <div class="brand-name" style="top:134px">Interactie Group</div>

    <div class="banner-rail"></div>
    <div class="banner" role="img" aria-label="Banner photo of a close-up eye and a magnifying glass on a blue background">
      <div class="banner-tagline"><strong>Focusing on your brand</strong><span>With the right Internet Marketing tools</span></div>
    </div>

    <div class="service" style="left:-8px;top:228px"><div class="service-label is-magenta">Creative<br>Advertising</div></div>
    <div class="service" style="left:191px;top:228px"><div class="service-label is-green">Corporate<br>Identy</div></div>
    <div class="service" style="left:382px;top:225px"><div class="service-label is-blue">Print<br>Design</div></div>
    <div class="service" style="left:584px;top:228px"><div class="service-label is-black">Packaing</div></div>
    <div class="service" style="left:791px;top:228px"><div class="service-label is-orange">Web<br>Design</div></div>
    <div class="service" style="left:1000px;top:220px"><div class="service-label is-blue">E Commerce</div></div>

    <div class="service" style="left:21px;top:322px"><div class="service-label is-blue service-label--small">WebApplication<br>Development</div></div>
    <div class="service" style="left:223px;top:320px"><div class="service-label is-orange">Multimedia</div></div>
    <div class="service" style="left:420px;top:324px"><div class="service-label is-black">SEO</div></div>
    <div class="service" style="left:619px;top:324px"><div class="service-label is-blue">SEM<br>Pay per click</div></div>
    <div class="service" style="left:806px;top:320px"><div class="service-label is-green">E mail<br>Marketing</div></div>
    <div class="service" style="left:1000px;top:322px"><div class="service-label is-magenta service-label--tiny">Reputation<br>Repair<br>Management</div></div>
  </header>

  <main class="content">
    <section class="panel panel--about">
      <p class="about-lead"><span class="accent">Brellow Interactive Group</span> is a leading Dallas Web Site Design, Publishing and Internet Marketing Firm.<br>Our Dallas Texas based Website Design and Internet Marketing experts<br>&nbsp;are some of the best in the industry!</p>
      <p class="about-body"><span class="accent">Brellow Interactive Web</span> is a full-service Dallas based Advertising Agency<br>&nbsp;comprised of experienced advertising and marketing professionals that provide<br>clients with a clear and distinct voice in the marketplace. Web Site Design<br>and Internet Marketing experts at our Dallas location specialize in developing<br>Online Marketing Strategies, Search Engine Marketing and Optimization (SEO),<br>Pay Per Click , Web Site Design and Development, and Online Reputation Management.</p>
    </section>

    <aside class="panel panel--quote">
      <p class="quote-intro">Click on the link below to begin filling out our Request-A-Quote form</p>
      <a class="quote-button"><span>Request a<br>Quote</span></a>
      <div class="follow-title">Follow Us on</div>
      <ul class="social-list">
        <li class="social-item" aria-label="Pinroom"></li>
        <li class="social-item" aria-label="Folkpage"></li>
        <li class="social-item" aria-label="Chirpline"></li>
        <li class="social-item" aria-label="Wanderlink"></li>
        <li class="social-item" aria-label="News feed"></li>
        <li class="social-item" aria-label="Snapfold"></li>
      </ul>
    </aside>
  </main>
</div>
</body>
</html>
```